Flyer for Aluminium recycling business

We are a startup aluminium recycling business. We don’t have a logo yet. I’ve attached a flyer created by one of our sales people but it’s a bit average and we need something a bit more modern and slick. You have creative license to completely change everything - as long as the information being communicated is the same.

Target Market(s)

Hospitality, Hotels, Apartment blocks, malls etcs

Industry/Entity Type

Aluminium recycling

Requirements
Must have
• the wording
Nice to have
• you have free license on design aspect

```html
<!DOCTYPE html>
<html lang="en">
<head>
<meta charset="utf-8">
<title>Greenloop Reclaim – Aluminium Recycling Flyer</title>
<link href="https://fonts.googleapis.com/css2?family=Outfit:wght@400;500;600;700&display=swap" rel="stylesheet">
<style>
  :root{
    --backdrop:#a9a89b;
    --sun:#efc23c;
    --sun-deep:#e9b82e;
    --mark:#1f2a1a;
    --ink:#231a10;
    --mint-top:#def6d6;
    --mint-bottom:#f2fbee;
    --leaf:#4e9a06;
    --dash:#6b3a22;
    --alert:#f6c21a;
    --white:#ffffff;
  }
  *{margin:0;padding:0;box-sizing:border-box}
  html,body{width:916px;height:1200px;overflow:hidden;background:var(--backdrop)}
  body{font-family:"Outfit",sans-serif;color:var(--ink);position:relative}
  .flyer{position:absolute;left:48px;top:20px;width:820px;height:1160px;background:var(--mint-bottom);overflow:hidden}
  .hero{position:absolute;left:0;top:0;width:820px;height:495px;
    background:radial-gradient(ellipse at center,var(--sun) 45%,var(--sun-deep) 100%)}
  .hero-photos{position:absolute;inset:0}
  .brand{position:absolute;left:0;width:820px;top:146px;text-align:center}
  .brand-dot{display:block;width:84px;height:84px;margin:0 auto 22px;border-radius:50%;background:var(--mark)}
  .brand-name{font-family:"Outfit",sans-serif;font-weight:600;color:var(--mark);font-size:30px;line-height:34px;letter-spacing:2px;text-transform:uppercase}
  .tagline{position:absolute;left:0;width:820px;top:342px;text-align:center;font-weight:500;font-size:20px;line-height:25px;text-transform:uppercase;color:var(--ink)}
  .body-panel{position:absolute;left:0;top:495px;width:820px;height:608px;
    background:radial-gradient(ellipse at 70% 10%,var(--mint-top) 0%,var(--mint-bottom) 70%)}
  .cycle{position:absolute;left:0;top:0}
  .here{position:absolute;left:310px;width:200px;top:641px;text-align:center;font-weight:700;line-height:1}
  .here-small{font-size:27px;display:block}
  .here-big{font-size:50px;display:block;margin-top:2px}
  .partnership{position:absolute;left:40px;top:617px;font-weight:600;font-size:17.5px;line-height:18.7px;text-transform:uppercase;white-space:nowrap}
  .list-title{position:absolute;top:837px;font-weight:600;font-size:18px;text-transform:uppercase}
  .list{position:absolute;list-style:none;font-size:15px;line-height:15.5px}
  .list li{position:absolute;padding-left:32px;white-space:nowrap}
  .list li svg{position:absolute;left:0;top:0}
  .footer{position:absolute;left:0;top:1103px;width:820px;height:57px;background:var(--leaf);color:var(--white)}
  .phone{position:absolute;left:142px;top:9px;font-weight:500;font-size:31px;line-height:38px}
  .email{position:absolute;left:427px;top:13px;font-weight:500;font-size:22px;line-height:28px}
  .footer svg{position:absolute}
</style>
</head>
<body>
<main class="flyer">
  <section class="hero">
    <div class="hero-photos" role="img" aria-label="Crushed aluminium cans, foil, a tin lid, a takeaway tray and a bottle cap scattered on a yellow background"></div>
    <div class="brand">
      <span class="brand-dot"></span>
      <div class="brand-name">Greenloop<br>Reclaim</div>
    </div>
    <p class="tagline">Playing the fair aluminum recycling<br>game for good</p>
  </section>

  <section class="body-panel"></section>

  <svg class="cycle" width="820" height="1103" viewBox="0 0 820 1103" aria-hidden="true">
    <defs>
      <linearGradient id="greenBall" x1="0" y1="0" x2="0" y2="1">
        <stop offset="0" stop-color="#5fc03a"/><stop offset="1" stop-color="#2f8d2a"/>
      </linearGradient>
      <linearGradient id="barkBall" x1="0" y1="0" x2="0" y2="1">
        <stop offset="0" stop-color="#6e3b24"/><stop offset="1" stop-color="#4a2414"/>
      </linearGradient>
    </defs>
    <circle cx="410" cy="677" r="137" fill="none" stroke="var(--dash)" stroke-width="1.6" stroke-dasharray="5 4"/>
    <circle cx="410.5" cy="539" r="25" fill="url(#greenBall)"/>
    <path d="M410.5 527 l10 17 h-20 z" fill="none" stroke="#fff" stroke-width="2.6" stroke-linejoin="round"/>
    <circle cx="513.6" cy="590" r="25" fill="url(#greenBall)"/>
    <path d="M503 580 h21 M506 583 l2 18 h11 l2 -18" fill="none" stroke="#fff" stroke-width="2.4" stroke-linejoin="round"/>
    <circle cx="541.3" cy="679" r="25" fill="url(#greenBall)"/>
    <rect x="534" y="668" width="14" height="22" rx="3" fill="#dfe3e3"/>
    <circle cx="496.2" cy="778" r="25" fill="url(#greenBall)"/>
    <path d="M482 770 h18 v14 h-18 z M500 775 h7 l4 5 v4 h-11 z" fill="#fff"/>
    <circle cx="487" cy="786" r="2.5" fill="#fff"/><circle cx="505" cy="786" r="2.5" fill="#fff"/>
    <circle cx="405.3" cy="812" r="25" fill="url(#greenBall)"/>
    <path d="M392 823 v-12 l7 -5 v5 l7 -5 v17 z" fill="#f2c21a"/>
    <rect x="408" y="799" width="4" height="24" fill="#fff"/><rect x="414" y="802" width="4" height="21" fill="#fff"/>
    <circle cx="310" cy="770" r="25" fill="url(#barkBall)"/>
    <rect x="302" y="760" width="16" height="20" fill="#d9dcdc"/>
    <circle cx="279" cy="684.4" r="25" fill="url(#greenBall)"/>
    <circle cx="279" cy="684.4" r="11" fill="none" stroke="#fff" stroke-width="2.6" stroke-dasharray="14 4"/>
    <circle cx="299.6" cy="593.5" r="25" fill="url(#barkBall)"/>
    <rect x="292" y="585" width="16" height="11" rx="1.5" fill="#5cb34a"/>
    <rect x="286" y="595" width="8" height="6" rx="2" fill="#e7b48f"/>
  </svg>

  <p class="partnership">Our partnership<br>with you is based<br>on common<br>sense, mutual<br>gain and a better<br>tomorrow</p>

  <div class="here"><span class="here-small">YOU ARE</span><span class="here-big">HERE</span></div>

  <h2 class="list-title" style="left:39px">It’s simple</h2>
  <ul class="list" style="left:40px;top:0">
    <li style="top:879px"><svg width="18" height="16" viewBox="0 0 18 16"><path d="M12 2.5H2v12h12V9" fill="none" stroke="var(--ink)" stroke-width="2"/><path d="M4.5 7.5l3.5 3.5L17 1.5" fill="none" stroke="var(--ink)" stroke-width="2.2"/></svg>We bring you a free bin</li>
    <li style="top:908px"><svg width="18" height="16" viewBox="0 0 18 16"><path d="M12 2.5H2v12h12V9" fill="none" stroke="var(--ink)" stroke-width="2"/><path d="M4.5 7.5l3.5 3.5L17 1.5" fill="none" stroke="var(--ink)" stroke-width="2.2"/></svg>You throw all and any aluminium waste into<br>the bin - no need te super-clean it. Try to compact /<br>squash the aluminium as much possible</li>
    <li style="top:966px"><svg width="18" height="16" viewBox="0 0 18 16"><path d="M12 2.5H2v12h12V9" fill="none" stroke="var(--ink)" stroke-width="2"/><path d="M4.5 7.5l3.5 3.5L17 1.5" fill="none" stroke="var(--ink)" stroke-width="2.2"/></svg>We collect the bin at no charge</li>
    <li style="top:995px"><svg width="18" height="16" viewBox="0 0 18 16"><path d="M12 2.5H2v12h12V9" fill="none" stroke="var(--ink)" stroke-width="2"/><path d="M4.5 7.5l3.5 3.5L17 1.5" fill="none" stroke="var(--ink)" stroke-width="2.2"/></svg>We turn the aluminium waste into a desirable<br>resource</li>
    <li style="top:1037px"><svg width="18" height="16" viewBox="0 0 18 16"><path d="M12 2.5H2v12h12V9" fill="none" stroke="var(--ink)" stroke-width="2"/><path d="M4.5 7.5l3.5 3.5L17 1.5" fill="none" stroke="var(--ink)" stroke-width="2.2"/></svg>We pay you for however much of that resource your<br>waste has generated - and give you a report on that, so<br>you can see how good you are</li>
  </ul>

  <h2 class="list-title" style="left:472px">Examples of what we can take</h2>
  <ul class="list" style="left:474px;top:0">
    <li style="top:879px;padding-left:30px"><svg width="18" height="16" viewBox="0 0 18 16"><path d="M12 2.5H2v12h12V9" fill="none" stroke="var(--ink)" stroke-width="2"/><path d="M4.5 7.5l3.5 3.5L17 1.5" fill="none" stroke="var(--ink)" stroke-width="2.2"/></svg>Used beverage cans - any</li>
    <li style="top:908px;padding-left:30px"><svg width="18" height="16" viewBox="0 0 18 16"><path d="M12 2.5H2v12h12V9" fill="none" stroke="var(--ink)" stroke-width="2"/><path d="M4.5 7.5l3.5 3.5L17 1.5" fill="none" stroke="var(--ink)" stroke-width="2.2"/></svg>Tinfoil - scrunched, crusty, burned or dirty</li>
    <li style="top:936px;padding-left:30px"><svg width="18" height="16" viewBox="0 0 18 16"><path d="M12 2.5H2v12h12V9" fill="none" stroke="var(--ink)" stroke-width="2"/><path d="M4.5 7.5l3.5 3.5L17 1.5" fill="none" stroke="var(--ink)" stroke-width="2.2"/></svg>Disposable BBQ roasting trays</li>
    <li style="top:965px;padding-left:30px"><svg width="18" height="16" viewBox="0 0 18 16"><path d="M12 2.5H2v12h12V9" fill="none" stroke="var(--ink)" stroke-width="2"/><path d="M4.5 7.5l3.5 3.5L17 1.5" fill="none" stroke="var(--ink)" stroke-width="2.2"/></svg>Aluminium takeaway containers</li>
    <li style="top:994px;padding-left:30px"><svg width="18" height="16" viewBox="0 0 18 16"><path d="M12 2.5H2v12h12V9" fill="none" stroke="var(--ink)" stroke-width="2"/><path d="M4.5 7.5l3.5 3.5L17 1.5" fill="none" stroke="var(--ink)" stroke-width="2.2"/></svg>Wine bottle screw tops (and collars - if<br>you can get them off)</li>
    <li style="top:1039px;padding-left:30px"><svg width="18" height="16" viewBox="0 0 18 16"><path d="M12 2.5H2v12h12V9" fill="none" stroke="var(--ink)" stroke-width="2"/><path d="M4.5 7.5l3.5 3.5L17 1.5" fill="none" stroke="var(--ink)" stroke-width="2.2"/></svg>Tear-off can lids</li>
  </ul>

  <footer class="footer">
    <svg style="left:94px;top:12px" width="32" height="32" viewBox="0 0 24 24" aria-hidden="true">
      <path d="M6.6 10.8a15.2 15.2 0 0 0 6.6 6.6l2.2-2.2a1 1 0 0 1 1-.25 11.4 11.4 0 0 0 3.6.57 1 1 0 0 1 1 1V20a1 1 0 0 1-1 1A17 17 0 0 1 3 4a1 1 0 0 1 1-1h3.5a1 1 0 0 1 1 1c0 1.25.2 2.45.57 3.57a1 1 0 0 1-.25 1z" fill="var(--alert)"/>
      <path d="M14 2.5a7.5 7.5 0 0 1 7.5 7.5M14 6a4 4 0 0 1 4 4" fill="none" stroke="var(--alert)" stroke-width="1.8"/>
    </svg>
    <span class="phone">021 555 0172</span>
    <svg style="left:378px;top:16px" width="32" height="24" viewBox="0 0 32 24" aria-hidden="true">
      <rect x="1" y="1" width="30" height="22" fill="var(--alert)"/>
      <path d="M1 1l15 12L31 1M1 23l11-10M31 23L20 13" fill="none" stroke="var(--leaf)" stroke-width="1.6"/>
    </svg>
    <span class="email">hello@greenloopreclaim.co.nz</span>
  </footer>
</main>
</body>
</html>
```